Canola Oil Packing Design for catering industry

Hong Kong based edible oil distributor, we would like to have a new packing design for our canola oil steel tin
Feel: easily let people know that the product is from canada; healthy and fresh feel
This packing is for catering market, like hotel, clubs & restaurants
Size: 4 faces in total = 895mm x 355mm allow 6mm for top and bottom, see steel tin sample attached, each size see same graphic
Final output: please provide both ai and pdf file

Target Market(s)

whole sale catering market

Industry/Entity Type

Catering

Font styles to use
Other font styles liked:
• designer choose

Requirements
Must have
• Brand name: Verhollin
• Product name: Canola Oil
• "HACCP certified" wording with icon
• Nutrition information: see file, please use the content and make it look nice, make it looks more or less the same as USA BRQ format: http://www.pelmarquist.org/Items/AdvisoryNotes/ReferencePagesGuideArchiveMaterial/PanelFormats/ref482173.htm
• Product info: see file, please use the content and make it look nice
Nice to have
• canada feel or even canada flag
Should not have
• copy from the others please

```html
<!DOCTYPE html>
<html lang="en">
<head>
<meta charset="utf-8">
<title>Verhollin Canola Oil – Tin Wrap, 4 Faces</title>
<link rel="stylesheet" href="https://fonts.googleapis.com/css2?family=Oswald:wght@500;700&family=Kaushan+Script&family=Roboto:wght@400;700;900&display=swap">
<style>
  :root {
    --bg: #d9d9d9;
    --label-yellow: #f6d21c;
    --label-yellow-light: #fbe76a;
    --label-yellow-deep: #e9b40c;
    --brand-green: #2f7d1f;
    --product-red: #d0261c;
    --claim-red: #c8201a;
    --oil-gold: #f3b619;
    --oil-amber: #d98b0a;
    --petal-yellow: #ffe23a;
    --leaf-green: #6c9a2a;
    --ink: #1b1b1b;
    --panel-line: rgba(0,0,0,0.12);
    --white: #ffffff;
  }
  * { box-sizing: border-box; margin: 0; padding: 0; }
  html, body { width: 900px; height: 1200px; overflow: hidden; }
  body {
    background: var(--bg);
    display: flex;
    align-items: center;
    justify-content: center;
    font-family: "Roboto", Arial, sans-serif;
  }
  .tin-wrap {
    width: 880px;
    height: 349px;
    display: grid;
    grid-template-columns: repeat(4, 1fr);
    box-shadow: 0 6px 18px rgba(0,0,0,0.25);
  }
  .panel {
    position: relative;
    overflow: hidden;
    background: radial-gradient(ellipse at 40% 35%, var(--label-yellow-light) 0%, var(--label-yellow) 55%, var(--label-yellow-deep) 100%);
    border-right: 1px solid var(--panel-line);
  }
  .panel:last-child { border-right: 0; }

  .maker-mark {
    position: absolute; top: 10px; left: 12px;
    display: flex; align-items: center; gap: 3px;
    font-family: "Roboto", Arial, sans-serif; font-weight: 700;
    font-size: 7px; color: var(--brand-green);
  }
  .maker-mark .dot { width: 9px; height: 9px; background: var(--brand-green); }

  .brand-name {
    position: absolute; left: 14px; top: 22px;
    font-family: "Oswald", Arial, sans-serif; font-weight: 700;
    font-size: 34px; line-height: 1; color: var(--brand-green);
    letter-spacing: 0.5px;
  }
  .product-name {
    position: absolute; left: 16px; top: 60px;
    font-family: "Oswald", Arial, sans-serif; font-weight: 700;
    font-size: 18px; line-height: 1; color: var(--product-red);
  }
  .oil-splash {
    position: absolute; left: -10px; top: 78px; width: 240px; height: 46px;
    background: linear-gradient(100deg, transparent 0%, var(--oil-gold) 25%, var(--oil-amber) 60%, var(--oil-gold) 85%, transparent 100%);
    border-radius: 50% 50% 45% 55%;
    transform: rotate(-6deg);
    opacity: 0.85;
  }
  .claims {
    position: absolute; left: 22px; top: 130px;
    font-family: "Kaushan Script", cursive; font-size: 13px;
    line-height: 1.2; color: var(--claim-red);
    list-style: none;
  }
  .haccp-badge {
    position: absolute; left: 16px; top: 200px;
    width: 30px; height: 30px; border-radius: 50%;
    background: var(--brand-green);
  }
  .origin-flag {
    position: absolute; left: 16px; top: 240px;
    width: 22px; height: 12px; background: var(--product-red);
  }
  .flower-art {
    position: absolute; right: -6px; bottom: 24px; width: 130px; height: 118px;
    background: radial-gradient(circle at 40% 45%, var(--petal-yellow) 0%, var(--oil-gold) 45%, var(--leaf-green) 90%, transparent 100%);
    border-radius: 50% 40% 45% 50%;
  }
  .net-volume {
    position: absolute; left: 14px; bottom: 10px;
    font-size: 7px; font-weight: 700; color: var(--ink);
  }

  /* information face */
  .panel--info .brand-name { font-size: 28px; }
  .panel--info .product-name { top: 52px; font-size: 15px; }
  .panel--info .oil-splash { top: 68px; height: 30px; opacity: 0.7; }
  .info-copy {
    position: absolute; left: 12px; top: 112px; width: 82px;
    font-size: 6.5px; line-height: 1.45; color: var(--ink);
  }
  .info-copy p + p { margin-top: 5px; }
  .nutrition-facts {
    position: absolute; right: 10px; top: 108px; width: 108px;
    background: var(--white); border: 1px solid var(--ink);
    padding: 3px 4px; color: var(--ink);
    font-size: 6px; line-height: 1.35;
  }
  .nutrition-facts h3 {
    font-family: "Roboto", Arial, sans-serif; font-weight: 900;
    font-size: 10px; line-height: 1.1;
    border-bottom: 1px solid var(--ink); padding-bottom: 1px;
  }
  .nutrition-facts .serving { border-bottom: 4px solid var(--ink); padding: 1px 0 2px; }
  .nutrition-facts table { width: 100%; border-collapse: collapse; }
  .nutrition-facts td { border-bottom: 0.5px solid var(--ink); padding: 1px 0; }
  .nutrition-facts td.value { text-align: right; }
  .nutrition-facts tr.major td { font-weight: 700; }
  .nutrition-facts tr.sub td:first-child { padding-left: 6px; }
  .nutrition-facts tr:last-child td { border-bottom: 0; }
  .panel--info .flower-art { width: 70px; height: 62px; left: 10px; right: auto; bottom: 26px; }
</style>
</head>
<body>
  <main class="tin-wrap">

    <section class="panel panel--front">
      <div class="maker-mark"><span class="dot"></span>Verhollin</div>
      <h1 class="brand-name">Verhollin</h1>
      <h2 class="product-name">Canola Oil</h2>
      <div class="oil-splash" role="img" aria-label="Golden oil splash"></div>
      <ul class="claims">
        <li>No Preservatives</li>
        <li>Cholesterol Free</li>
        <li>100% Natural</li>
      </ul>
      <div class="haccp-badge" role="img" aria-label="HACCP certified badge"></div>
      <div class="origin-flag" role="img" aria-label="Canadian flag"></div>
      <div class="flower-art" role="img" aria-label="Yellow canola flowers"></div>
      <p class="net-volume">NET 18 L</p>
    </section>

    <section class="panel panel--info">
      <h1 class="brand-name">Verhollin</h1>
      <h2 class="product-name">Canola Oil</h2>
      <div class="oil-splash" role="img" aria-label="Golden oil splash"></div>
      <div class="info-copy">
        <p>Ingredients: 100% pure canola oil</p>
        <p>Store in a cool dry place</p>
        <p>Product of Canada</p>
      </div>
      <div class="nutrition-facts">
        <h3>Nutrition Facts</h3>
        <p class="serving">Serving Size 1 tbsp (14g)</p>
        <table>
          <tr class="major"><td>Calories</td><td class="value">120</td></tr>
          <tr class="major"><td>Total Fat</td><td class="value">14g</td></tr>
          <tr class="sub"><td>Saturated Fat</td><td class="value">1g</td></tr>
          <tr class="sub"><td>Trans Fat</td><td class="value">0g</td></tr>
          <tr class="major"><td>Cholesterol</td><td class="value">0mg</td></tr>
          <tr class="major"><td>Sodium</td><td class="value">0mg</td></tr>
          <tr class="major"><td>Total Carbohydrate</td><td class="value">0g</td></tr>
          <tr class="major"><td>Protein</td><td class="value">0g</td></tr>
        </table>
      </div>
      <div class="flower-art" role="img" aria-label="Yellow canola flowers"></div>
    </section>

    <section class="panel panel--front">
      <div class="maker-mark"><span class="dot"></span>Verhollin</div>
      <h1 class="brand-name">Verhollin</h1>
      <h2 class="product-name">Canola Oil</h2>
      <div class="oil-splash" role="img" aria-label="Golden oil splash"></div>
      <ul class="claims">
        <li>No Preservatives</li>
        <li>Cholesterol Free</li>
        <li>100% Natural</li>
      </ul>
      <div class="haccp-badge" role="img" aria-label="HACCP certified badge"></div>
      <div class="origin-flag" role="img" aria-label="Canadian flag"></div>
      <div class="flower-art" role="img" aria-label="Yellow canola flowers"></div>
      <p class="net-volume">NET 18 L</p>
    </section>

    <section class="panel panel--info">
      <h1 class="brand-name">Verhollin</h1>
      <h2 class="product-name">Canola Oil</h2>
      <div class="oil-splash" role="img" aria-label="Golden oil splash"></div>
      <div class="info-copy">
        <p>Ingredients: 100% pure canola oil</p>
        <p>Store in a cool dry place</p>
        <p>Product of Canada</p>
      </div>
      <div class="nutrition-facts">
        <h3>Nutrition Facts</h3>
        <p class="serving">Serving Size 1 tbsp (14g)</p>
        <table>
          <tr class="major"><td>Calories</td><td class="value">120</td></tr>
          <tr class="major"><td>Total Fat</td><td class="value">14g</td></tr>
          <tr class="sub"><td>Saturated Fat</td><td class="value">1g</td></tr>
          <tr class="sub"><td>Trans Fat</td><td class="value">0g</td></tr>
          <tr class="major"><td>Cholesterol</td><td class="value">0mg</td></tr>
          <tr class="major"><td>Sodium</td><td class="value">0mg</td></tr>
          <tr class="major"><td>Total Carbohydrate</td><td class="value">0g</td></tr>
          <tr class="major"><td>Protein</td><td class="value">0g</td></tr>
        </table>
      </div>
      <div class="flower-art" role="img" aria-label="Yellow canola flowers"></div>
    </section>

  </main>
</body>
</html>
```